Stationary Design using supplied logo

24 Hour Completion required after acceptance

Business Cards
Letter Head
With Compliments Slips
Web Page Theme

Please only use a the following colors:

Red
Charcoal
Chrome/Silver
White

Red being the DOMINANT Color

Please email questions you may have.

Continued work available to suitably motivated designer.

```html
<!DOCTYPE html>
<html lang="en">
<head>
<meta charset="utf-8">
<title>Kinfold Lending – Stationery</title>
<link rel="stylesheet" href="https://fonts.googleapis.com/css2?family=Source+Sans+3:wght@300;400;600&display=swap">
<style>
  :root {
    --red: #c8102e;
    --charcoal: #333333;
    --card-dark: #353535;
    --silver: #9a9a9a;
    --white: #ffffff;
    --text: #3a3a3a;
    --edge: #c9c9c9;
  }
  * { box-sizing: border-box; margin: 0; padding: 0; }
  html, body { width: 1200px; height: 900px; overflow: hidden; }
  body {
    background: var(--white);
    font-family: "Source Sans 3", Arial, sans-serif;
    font-weight: 400;
    color: var(--text);
    position: relative;
  }
  .piece {
    position: absolute;
    background: var(--white);
    border: 1px solid var(--edge);
    box-shadow: 1px 2px 3px rgba(0,0,0,.25);
    overflow: hidden;
  }
  .piece.dark { background: var(--card-dark); border-color: #2a2a2a; color: #e8e8e8; }
  .swoosh { position: absolute; left: 0; width: 100%; display: block; }
  .band-silver { fill: var(--silver); }
  .band-red { fill: var(--red); }

  .brand {
    position: absolute;
    font-weight: 300;
    color: var(--charcoal);
    line-height: 1;
    white-space: nowrap;
    letter-spacing: -.01em;
  }

  .label { color: var(--red); }
  .contact { position: absolute; line-height: 1.2; white-space: nowrap; }
  .contact .gap { margin-top: .9em; }
  .offices { position: absolute; white-space: nowrap; text-align: center; }
  .offices .sep { margin: 0 .6em; }

  /* Letterhead */
  .letterhead { left: 22px; top: 18px; width: 617px; height: 871px; }
  .letterhead .swoosh { top: 50px; height: 112px; }
  .letterhead .contact { left: 480px; top: 37px; font-size: 8.5px; }
  .letterhead .brand { left: 46px; top: 103px; font-size: 30px; }
  .letterhead .offices { left: 0; width: 100%; bottom: 11px; font-size: 8.5px; }

  /* Compliments slip */
  .comp-slip { left: 569px; top: 212px; width: 596px; height: 282px; }
  .comp-slip .swoosh { top: 28px; height: 108px; }
  .comp-slip .contact { left: 464px; top: 16px; font-size: 8.5px; }
  .comp-slip .brand { left: 44px; top: 77px; font-size: 29px; }
  .comp-slip .offices { left: 0; width: 100%; bottom: 9px; font-size: 8.5px; }

  /* Business card fronts */
  .card-front { display: flex; align-items: center; justify-content: center; }
  .card-front .brand { position: static; }
  .card-front.landscape { left: 569px; top: 506px; width: 242px; height: 157px; }
  .card-front.landscape .brand { font-size: 24px; }
  .card-front.portrait { left: 1007px; top: 552px; width: 158px; height: 242px; }
  .card-front.portrait .brand { font-size: 18px; }

  /* Business card backs */
  .person-name { position: absolute; color: var(--red); font-weight: 600; font-size: 11px; line-height: 1; }
  .person-role { position: absolute; color: #e0e0e0; font-size: 9px; line-height: 1; }
  .card-back .contact, .card-back .offices { font-size: 6.3px; color: #dcdcdc; text-align: left; }

  .card-back.landscape { left: 569px; top: 683px; width: 242px; height: 156px; }
  .card-back.landscape .person-name { left: 10px; top: 49px; }
  .card-back.landscape .person-role { left: 10px; top: 62px; }
  .card-back.landscape .swoosh { top: 76px; height: 42px; }
  .card-back.landscape .phones { left: 10px; top: 96px; }
  .card-back.landscape .web { left: 10px; top: 120px; }
  .card-back.landscape .offices { left: 118px; top: 120px; line-height: 1.2; }

  .card-back.portrait { left: 830px; top: 552px; width: 158px; height: 242px; }
  .card-back.portrait .person-name { left: 10px; top: 84px; }
  .card-back.portrait .person-role { left: 10px; top: 97px; }
  .card-back.portrait .swoosh { top: 112px; height: 32px; }
  .card-back.portrait .phones { left: 10px; top: 131px; }
  .card-back.portrait .web { left: 10px; top: 172px; }
  .card-back.portrait .offices { left: 10px; top: 198px; line-height: 1.2; }
</style>
</head>
<body>

<!-- Letterhead -->
<section class="piece letterhead" aria-label="Letterhead">
  <svg class="swoosh" viewBox="0 0 100 30" preserveAspectRatio="none" aria-hidden="true">
    <path class="band-silver" d="M0,1.2 C35,-1 70,8 100,21.5 L100,26 C70,12 35,1 0,1.7 Z"/>
    <path class="band-red" d="M0,1.4 C35,-0.4 70,10 100,24.5 L100,30 C70,15 35,2 0,2.3 Z"/>
  </svg>
  <div class="contact">
    <p><span class="label">T:</span> 02 6100 4000</p>
    <p><span class="label">F:</span> 02 6100 4022</p>
    <p><span class="label">E:</span> hello@kinfoldlending.com.au</p>
    <p class="gap"><span class="label">W:</span> harrowfinance.com.au</p>
    <p><span class="label">P:</span> PO Box 1200 Marlow DC 2600</p>
  </div>
  <div class="brand">Kinfold Lending</div>
  <p class="offices"><span class="label">Head Office:</span> Fenwick St Marlow<span class="sep">.</span><span class="label">Brayfield:</span> Cnr Osler St &amp; Tanner Cres Hale<span class="sep">.</span><span class="label">Carrow:</span> Linden Chambers Carrow</p>
</section>

<!-- With compliments slip -->
<section class="piece comp-slip" aria-label="With compliments slip">
  <svg class="swoosh" viewBox="0 0 100 30" preserveAspectRatio="none" aria-hidden="true">
    <path class="band-silver" d="M0,1.2 C35,-1 70,8 100,21.5 L100,26 C70,12 35,1 0,1.7 Z"/>
    <path class="band-red" d="M0,1.4 C35,-0.4 70,10 100,24.5 L100,30 C70,15 35,2 0,2.3 Z"/>
  </svg>
  <div class="contact">
    <p><span class="label">T:</span> 02 6100 4000</p>
    <p><span class="label">F:</span> 02 6100 4022</p>
    <p><span class="label">E:</span> hello@kinfoldlending.com.au</p>
    <p class="gap"><span class="label">W:</span> harrowfinance.com.au</p>
    <p><span class="label">P:</span> PO Box 1200 Marlow DC 2600</p>
  </div>
  <div class="brand">Kinfold Lending</div>
  <p class="offices"><span class="label">Head Office:</span> Fenwick St Marlow<span class="sep">.</span><span class="label">Brayfield:</span> Cnr Osler St &amp; Tanner Cres Hale<span class="sep">.</span><span class="label">Carrow:</span> Linden Chambers Carrow</p>
</section>

<!-- Landscape business card -->
<section class="piece card-front landscape" aria-label="Business card front">
  <div class="brand">Kinfold Lending</div>
</section>

<section class="piece dark card-back landscape" aria-label="Business card back">
  <p class="person-name">Daniel Harrow</p>
  <p class="person-role">Managing Director</p>
  <svg class="swoosh" viewBox="0 0 100 30" preserveAspectRatio="none" aria-hidden="true">
    <path class="band-silver" d="M0,1.2 C35,-1 70,8 100,21.5 L100,26 C70,12 35,1 0,1.7 Z"/>
    <path class="band-red" d="M0,1.4 C35,-0.4 70,10 100,24.5 L100,30 C70,15 35,2 0,2.3 Z"/>
  </svg>
  <div class="contact phones">
    <p><span class="label">T:</span> 02 6100 4000</p>
    <p><span class="label">F:</span> 02 6100 4022</p>
  </div>
  <div class="contact web">
    <p><span class="label">E:</span> hello@kinfoldlending.com.au</p>
    <p><span class="label">W:</span> harrowfinance.com.au</p>
    <p><span class="label">P:</span> PO Box 1200 Marlow DC 2600</p>
  </div>
  <div class="offices">
    <p><span class="label">Head Office:</span> Fenwick St Marlow</p>
    <p><span class="label">Brayfield:</span> Cnr Osler St &amp; Tanner Cres Hale</p>
    <p><span class="label">Carrow:</span> Linden Chambers Carrow</p>
  </div>
</section>

<!-- Portrait business card -->
<section class="piece dark card-back portrait" aria-label="Portrait business card back">
  <p class="person-name">Daniel Harrow</p>
  <p class="person-role">Managing Director</p>
  <svg class="swoosh" viewBox="0 0 100 30" preserveAspectRatio="none" aria-hidden="true">
    <path class="band-silver" d="M0,1.2 C35,-1 70,8 100,21.5 L100,26 C70,12 35,1 0,1.7 Z"/>
    <path class="band-red" d="M0,1.4 C35,-0.4 70,10 100,24.5 L100,30 C70,15 35,2 0,2.3 Z"/>
  </svg>
  <div class="contact phones">
    <p><span class="label">T:</span> 02 6100 4000</p>
    <p><span class="label">F:</span> 02 6100 4022</p>
    <p><span class="label">E:</span> hello@kinfoldlending.com.au</p>
  </div>
  <div class="contact web">
    <p><span class="label">W:</span> harrowfinance.com.au</p>
    <p><span class="label">P:</span> PO Box 1200 Marlow DC 2600</p>
  </div>
  <div class="offices">
    <p><span class="label">Head Office:</span> Fenwick St Marlow</p>
    <p><span class="label">Brayfield:</span> Cnr Osler St &amp; Tanner Cres Hale</p>
    <p><span class="label">Carrow:</span> Linden Chambers Carrow</p>
  </div>
</section>

<section class="piece card-front portrait" aria-label="Portrait business card front">
  <div class="brand">Kinfold Lending</div>
</section>

</body>
</html>
```